Runlark

I have a web site RUNLARK.com that is in serious need of a re-design. The site is mean't to be a portal for an app that I have called RUNLARK which you can see in the app store or googleplay. Take a look and see what you can do.
Updates

Project Deadline Extended
Reason: Still working with designers. The "look" is not quite there but a lot of progress has been made. MB

Industry/Entity Type

Store

```html
<!DOCTYPE html>
<html lang="en">
<head>
<meta charset="utf-8">
<title>Runlark — Sport Stats on Demand</title>
<link rel="stylesheet" href="https://fonts.googleapis.com/css2?family=Arimo:wght@400;700&family=Bitter:wght@700&family=Ubuntu:wght@400;500;700&family=Oswald:wght@400;500&display=swap">
<style>
:root{
  --green:#22bf00;
  --green-dark:#1a9a00;
  --navy:#1a3f7d;
  --ink:#222;
  --muted:#777;
  --light:#f0f0f0;
  --panel:#e6e6e6;
  --dark:#1b1b1b;
  --footer:#2a2a2a;
  --footer-deep:#1e1e1e;
  --white:#fff;
}
*{box-sizing:border-box;margin:0;padding:0}
html,body{width:729px;height:1200px;overflow:hidden;background:var(--white)}
body{font-family:"Arimo",Arial,sans-serif;color:var(--ink)}
.page{position:relative;width:729px;height:1200px;overflow:hidden}
.abs{position:absolute}

/* header */
.site-header{left:0;top:0;width:729px;height:58px;background:var(--light)}
.brand{left:63px;top:14px;display:flex;align-items:center;gap:6px;font-family:"Ubuntu",sans-serif;font-weight:700;font-size:24px;color:var(--navy)}
.brand-dot{width:14px;height:14px;border-radius:50%;background:var(--green)}
.nav{top:42px;font-size:8px;color:#444}
.nav.active{border-bottom:2px solid var(--navy);padding-bottom:3px}

/* hero */
.hero-media{left:62px;top:63px;width:605px;height:229px;background:linear-gradient(135deg,#2c2a28,#5a4a3a 45%,#8a2a22 75%,#3a3030)}
.play-ring{left:334px;top:152px;width:60px;height:60px;border-radius:50%;border:3px solid rgba(255,255,255,.55);background:rgba(60,60,60,.5)}
.play-ring::after{content:"";position:absolute;left:21px;top:14px;border-left:22px solid rgba(20,20,20,.85);border-top:13px solid transparent;border-bottom:13px solid transparent}
.hero-caption{left:62px;top:253px;width:540px;height:28px;background:rgba(20,30,50,.55);color:var(--white);font-size:14.5px;letter-spacing:.4px;padding:5px 5px}
.player-bar{left:62px;top:292px;width:605px;height:32px;background:var(--dark)}
.player-play{left:0;top:0;width:42px;height:32px;background:var(--green)}
.player-play::after{content:"";position:absolute;left:16px;top:9px;border-left:12px solid #111;border-top:7px solid transparent;border-bottom:7px solid transparent}
.player-time{left:53px;top:9px;color:var(--white);font-size:11px}
.progress{left:121px;top:14px;width:327px;height:4px;background:var(--white)}
.progress span{display:block;width:193px;height:4px;background:var(--green)}

/* video band */
.video-band{left:0;top:334px;width:729px;height:193px;background:var(--green)}
.video-card{top:344px;width:189px;height:172px;background:var(--white);border:1px solid #ccc}
.video-thumb{left:4px;top:3px;width:180px;height:88px;background:linear-gradient(135deg,#2a4a7a,#3a6aa8 50%,#c8ccd0)}
.mini-bar{left:4px;top:91px;width:180px;height:23px;background:var(--dark)}
.mini-play{left:0;top:0;width:28px;height:23px;background:var(--green)}
.mini-play::after{content:"";position:absolute;left:11px;top:7px;border-left:7px solid #111;border-top:4.5px solid transparent;border-bottom:4.5px solid transparent}
.mini-time{left:33px;top:2px;color:var(--white);font-size:5.5px}
.mini-track{left:33px;top:12px;width:112px;height:3px;background:var(--white)}
.mini-track span{display:block;width:66px;height:3px;background:var(--green)}
.card-title{left:14px;top:127px;font-family:"Bitter",serif;font-size:9.5px;color:#222}
.card-meta{left:4px;top:147px;width:180px;height:18px;border-top:1px solid #ddd;background:#f6f6f6}
.league{left:0;top:0;width:53px;height:18px;background:var(--green);color:var(--white);font-family:"Bitter",serif;font-size:11px;text-align:center;line-height:18px}
.card-date{left:60px;top:4px;font-family:"Bitter",serif;font-style:italic;font-weight:400;font-size:7.5px;color:#888}

/* trending */
.trend-tab{left:72px;top:542px;width:94px;height:19px;background:#9a9a9a;border-radius:4px 4px 0 0;color:var(--white);font-family:"Ubuntu",sans-serif;font-size:10px;padding:3px 8px;letter-spacing:-.3px}
.trend-panel{left:69px;top:561px;width:385px;height:183px;background:var(--panel);border-top:1px solid #bbb;border-radius:0 0 6px 6px}
.trend-thumb{top:578px;width:101px;height:101px;border-radius:5px}
.trend-text{top:686px;width:108px;font-size:7.5px;line-height:10.5px;color:#777;letter-spacing:-.3px}
.more{top:720px;width:48px;height:15px;background:#a8a8a8;border-radius:2px;color:var(--white);font-size:6.5px;line-height:15px;padding-left:10px}
.more span{position:absolute;right:0;top:0;width:14px;height:15px;background:var(--navy);color:var(--white);font-size:8px;text-align:center;line-height:15px}

/* writers */
.writers{left:480px;top:552px;width:183px;height:192px;border:1px solid #ccc;border-radius:5px;background:var(--white)}
.writers-head{left:0;top:0;width:181px;height:25px;background:#f2f2f2;border-bottom:1px solid #ddd;border-radius:5px 5px 0 0;font-family:"Ubuntu",sans-serif;font-size:10px;color:#555;padding:6px 0 0 34px;letter-spacing:-.3px}
.writers-head::before{content:"";position:absolute;left:13px;top:6px;width:12px;height:12px;border:1.5px solid #999;border-radius:50%}
.writer-thumb{left:9px;width:37px;height:37px}
.writer-name{left:53px;font-size:8px;color:var(--navy);letter-spacing:-.3px}
.writer-text{left:53px;width:125px;font-size:7.5px;line-height:10.5px;color:#777;letter-spacing:-.4px}
.writer-rule{left:9px;width:163px;height:1px;background:#ccc}

/* stats */
.stats-rule{top:776px;height:2px;background:var(--navy)}
.stats-heading{left:262px;top:765px;width:210px;text-align:center;font-family:"Ubuntu",sans-serif;font-weight:500;font-size:16.5px;color:var(--navy);letter-spacing:.4px}
.stat-card{top:802px;width:122px;height:155px}
.stat-tag{width:40px;height:14px;background:var(--green);color:#0c3a00;font-size:6.5px;font-weight:700;line-height:14px;padding-left:4px}
.stat-overlay{left:0;top:104px;width:122px;height:51px;background:rgba(25,25,25,.8);padding:6px 10px}
.stat-title{font-family:"Bitter",serif;font-size:8.5px;line-height:13px;color:var(--white)}
.stat-date{font-family:"Bitter",serif;font-style:italic;font-weight:400;font-size:6.5px;color:#ccc;margin-top:3px}

/* footer */
.footer-edge{left:0;top:975px;width:729px;height:4px;background:#c8c8c8}
.footer{left:0;top:979px;width:729px;height:194px;background:var(--footer)}
.foot-h{font-family:"Oswald",sans-serif;font-size:11.5px;color:var(--green);letter-spacing:-.2px}
.foot-list{list-style:none;font-size:7.5px;color:#aaa}
.foot-list li{height:18.8px;padding-left:11px;position:relative}
.foot-list li::before{content:"›";position:absolute;left:0;top:-2px;color:var(--green);font-size:9px}
.contact{font-size:7.5px;line-height:11px;color:#aaa}
.contact b{font-weight:400;color:var(--green)}
.social{top:1123px;width:25px;height:25px;background:#5a5a5a;border:1px solid #777}
.footer-base{left:0;top:1173px;width:729px;height:27px;background:var(--footer-deep)}
.base-text{top:1183px;font-size:7.5px;color:#999}
.store-badge{left:608px;top:1177px;width:57px;height:20px;background:#8a8a8a;border-radius:3px;border:1px solid #aaa}
</style>
</head>
<body>
<div class="page">

  <header class="site-header abs"></header>
  <div class="brand abs"><span class="brand-dot"></span>Runlark</div>
  <span class="nav active abs" style="left:534px">Homepage</span>
  <span class="nav abs" style="left:598px">FAQ</span>
  <span class="nav abs" style="left:640px">Contact</span>

  <section>
    <div class="hero-media abs" role="img" aria-label="Football match photo: players celebrating a goal in front of a crowd"></div>
    <div class="play-ring abs"></div>
    <div class="hero-caption abs">The sport statistics and information you want when you want them</div>
    <div class="player-bar abs">
      <div class="player-play abs"></div>
      <span class="player-time abs">00:25 / 4:20</span>
      <div class="progress abs"><span></span></div>
      <svg class="abs" style="left:505px;top:9px" width="80" height="14" viewBox="0 0 80 14">
        <path d="M0 4h4l5-4v14l-5-4H0z" fill="#fff"/>
        <path d="M11 3q3 4 0 8" stroke="#fff" fill="none"/>
        <g fill="#22bf00"><rect x="20" y="4" width="2" height="7"/><rect x="24" y="4" width="2" height="7"/><rect x="28" y="4" width="2" height="7"/><rect x="32" y="4" width="2" height="7"/></g>
        <g fill="#fff"><rect x="36" y="4" width="2" height="7"/><rect x="40" y="4" width="2" height="7"/><rect x="44" y="4" width="2" height="7"/><rect x="48" y="4" width="2" height="7"/></g>
      </svg>
      <svg class="abs" style="left:731px;top:0" width="0" height="0"></svg>
      <svg class="abs" style="left:572px;top:8px" width="20" height="16" viewBox="0 0 20 16"><rect x="1" y="1" width="18" height="14" fill="none" stroke="#fff" stroke-width="1.5"/><rect x="5" y="5" width="10" height="6" fill="#fff"/></svg>
    </div>
  </section>

  <section class="video-band abs"></section>
  <article class="video-card abs" style="left:62px">
    <div class="video-thumb abs" role="img" aria-label="Football players in a tackle"></div>
    <div class="mini-bar abs"><div class="mini-play abs"></div><span class="mini-time abs">00:25 / 4:20</span><div class="mini-track abs"><span></span></div></div>
    <span class="card-title abs">Lorem ipsum dolor sit amet</span>
    <div class="card-meta abs"><span class="league abs">GFL</span><span class="card-date abs">September 9 2013 11:06</span></div>
  </article>
  <article class="video-card abs" style="left:272px">
    <div class="video-thumb abs" role="img" aria-label="Football players in a tackle"></div>
    <div class="mini-bar abs"><div class="mini-play abs"></div><span class="mini-time abs">00:25 / 4:20</span><div class="mini-track abs"><span></span></div></div>
    <span class="card-title abs">Lorem ipsum dolor sit amet</span>
    <div class="card-meta abs"><span class="league abs">GFL</span><span class="card-date abs">September 9 2013 11:06</span></div>
  </article>
  <article class="video-card abs" style="left:479px">
    <div class="video-thumb abs" role="img" aria-label="Football players in a tackle"></div>
    <div class="mini-bar abs"><div class="mini-play abs"></div><span class="mini-time abs">00:25 / 4:20</span><div class="mini-track abs"><span></span></div></div>
    <span class="card-title abs">Lorem ipsum dolor sit amet</span>
    <div class="card-meta abs"><span class="league abs">GFL</span><span class="card-date abs">September 9 2013 11:06</span></div>
  </article>

  <section>
    <div class="trend-panel abs"></div>
    <div class="trend-tab abs">Trending Content</div>
    <div class="trend-thumb abs" style="left:81px;background:linear-gradient(135deg,#5a4030,#8a4a2a 50%,#3a4a3a)" role="img" aria-label="Football player running with the ball"></div>
    <div class="trend-thumb abs" style="left:211px;background:linear-gradient(135deg,#b8c0b0,#6a8a4a 50%,#d8d8d0)" role="img" aria-label="Football player in a white jersey carrying the ball"></div>
    <div class="trend-thumb abs" style="left:340px;background:linear-gradient(135deg,#3a2a20,#8a4020 50%,#2a2a2a)" role="img" aria-label="Football player in helmet on the field"></div>
    <p class="trend-text abs" style="left:80px">Lorem ipsum dolor sit amet, consectetuer adipiscing elit, sed diam nonummy nibh</p>
    <p class="trend-text abs" style="left:213px">Lorem ipsum dolor sit amet, consectetuer adipiscing elit, sed diam nonummy nibh</p>
    <p class="trend-text abs" style="left:340px">Lorem ipsum dolor sit amet, consectetuer adipiscing elit, sed diam nonummy nibh</p>
    <a class="more abs" style="left:80px">more<span>»</span></a>
    <a class="more abs" style="left:213px">more<span>»</span></a>
    <a class="more abs" style="left:340px">more<span>»</span></a>
  </section>

  <aside class="writers abs">
    <div class="writers-head abs">Featured Writers</div>
    <div class="writer-thumb abs" style="top:32px;background:linear-gradient(135deg,#c8ccd0,#5a6a8a)" role="img" aria-label="Baseball pitcher photo"></div>
    <span class="writer-name abs" style="top:32px">Lorem ipsum</span>
    <p class="writer-text abs" style="top:44px">Lorem ipsum dolor sit amet, consectetuer adipiscing elit, sed diam</p>
    <div class="writer-rule abs" style="top:84px"></div>
    <div class="writer-thumb abs" style="top:88px;background:linear-gradient(135deg,#a03030,#3a5aa0)" role="img" aria-label="Baseball player photo"></div>
    <span class="writer-name abs" style="top:88px">Lorem ipsum</span>
    <p class="writer-text abs" style="top:100px">Lorem ipsum dolor sit amet, consectetuer adipiscing elit, sed diam</p>
    <div class="writer-rule abs" style="top:139px"></div>
    <div class="writer-thumb abs" style="top:143px;background:linear-gradient(135deg,#6a8a5a,#3a5aa0)" role="img" aria-label="Baseball fielder photo"></div>
    <span class="writer-name abs" style="top:143px">Lorem ipsum</span>
    <p class="writer-text abs" style="top:155px">Lorem ipsum dolor sit amet, consectetuer adipiscing elit, sed diam</p>
  </aside>

  <section>
    <div class="stats-rule abs" style="left:70px;width:192px"></div>
    <h2 class="stats-heading abs">Sport Stats on Demand</h2>
    <div class="stats-rule abs" style="left:472px;width:189px"></div>

    <article class="stat-card abs" style="left:71px;background:linear-gradient(160deg,#c8d0d8,#3a4a6a 55%,#2a2a2a)" role="img" aria-label="Football players in a tackle">
      <div class="stat-overlay abs"><p class="stat-title">Lorem ipsum dolor sit amet, consectetur...</p><p class="stat-date">September 11 2013</p></div>
    </article>
    <article class="stat-card abs" style="left:228px;background:linear-gradient(160deg,#1a1a1a,#6a4a3a 55%,#2a2a2a)" role="img" aria-label="Fighter raising his arm in victory">
      <div class="stat-overlay abs"><p class="stat-title">Lorem ipsum dolor sit amet, consectetur...</p><p class="stat-date">September 11 2013</p></div>
    </article>
    <article class="stat-card abs" style="left:382px;background:linear-gradient(160deg,#c8ccd0,#c85a2a 50%,#3a4a6a)" role="img" aria-label="Baseball batter swinging">
      <div class="stat-overlay abs"><p class="stat-title">Lorem ipsum dolor sit amet, consectetur...</p><p class="stat-date">September 11 2013</p></div>
    </article>
    <article class="stat-card abs" style="left:541px;background:linear-gradient(160deg,#1a1a1a,#a07a2a 55%,#2a2a2a)" role="img" aria-label="Basketball players going for a shot">
      <div class="stat-overlay abs"><p class="stat-title">Lorem ipsum dolor sit amet, consectetur...</p><p class="stat-date">September 11 2013</p></div>
    </article>
    <span class="stat-tag abs" style="left:65px;top:812px">Runlark</span>
    <span class="stat-tag abs" style="left:222px;top:812px">Runlark</span>
    <span class="stat-tag abs" style="left:376px;top:812px">Runlark</span>
    <span class="stat-tag abs" style="left:535px;top:812px">Runlark</span>
  </section>

  <div class="footer-edge abs"></div>
  <footer class="footer abs"></footer>

  <h3 class="foot-h abs" style="left:68px;top:996px">GFL NEWS</h3>
  <ul class="foot-list abs" style="left:68px;top:1019px"><li>Teams</li><li>Fantasy</li><li>Rumors</li></ul>
  <h3 class="foot-h abs" style="left:68px;top:1088px">HOCKEY NEWS</h3>
  <ul class="foot-list abs" style="left:68px;top:1111px"><li>Teams</li><li>Fantasy</li><li>Rumors</li></ul>

  <h3 class="foot-h abs" style="left:158px;top:996px">BASEBALL NEWS</h3>
  <ul class="foot-list abs" style="left:158px;top:1019px"><li>Teams</li><li>Fantasy</li><li>Rumors</li></ul>
  <h3 class="foot-h abs" style="left:158px;top:1088px">HOOPS NEWS</h3>
  <ul class="foot-list abs" style="left:158px;top:1111px"><li>Teams</li><li>Fantasy</li><li>Rumors</li></ul>

  <h3 class="foot-h abs" style="left:251px;top:996px">COLLEGE FB</h3>
  <ul class="foot-list abs" style="left:251px;top:1019px"><li>Teams</li><li>Coastal</li><li>Midland 10</li><li>Prairie 12</li><li>Harbor East</li><li>Summit 12</li><li>Delta</li></ul>

  <h3 class="foot-h abs" style="left:340px;top:996px">COLLEGE BB</h3>
  <ul class="foot-list abs" style="left:340px;top:1019px"><li>Teams</li><li>Coastal</li><li>Midland 10</li><li>Prairie 12</li><li>Harbor East</li><li>Summit 12</li><li>Delta</li></ul>

  <h3 class="foot-h abs" style="left:437px;top:996px">MORE NEWS</h3>
  <ul class="foot-list abs" style="left:437px;top:1019px"><li>Clubhouse</li><li>MMA</li><li>Pro Wrestling</li><li>Stock Car</li><li>Soccer</li><li>Golf</li><li>Prep Sports</li></ul>

  <h3 class="foot-h abs" style="left:541px;top:996px">CONTACT &nbsp;SUPPORT</h3>
  <address class="contact abs" style="left:541px;top:1019px;font-style:normal">2270 Meadowlark Rd.<br>Suite 410<br>Fairhaven, OH 44210<br><span style="display:block;height:6px"></span><b>Email :</b> info@runlark.com<br><span style="display:block;height:5px"></span><b>Phone :</b> (000) 000-0000</address>

  <h3 class="foot-h abs" style="left:541px;top:1099px">CONNECT WITH US</h3>
  <a class="social abs" style="left:542px" aria-label="Social profile 1"></a>
  <a class="social abs" style="left:571px" aria-label="Social profile 2"></a>
  <a class="social abs" style="left:600px" aria-label="Social profile 3"></a>
  <a class="social abs" style="left:629px" aria-label="Social profile 4"></a>

  <div class="footer-base abs"></div>
  <span class="base-text abs" style="left:68px">Privacy Policy &nbsp;| &nbsp;Terms of Use</span>
  <span class="base-text abs" style="left:520px">© 2013 by Runlark.</span>
  <div class="store-badge abs" aria-label="App store badge"></div>

</div>
</body>
</html>
```